New Content Rich Website Designs

We need an updated design layout for our website that is content rich.  Attached please find a document named Web Designer Instructions and also a New Home Page.   We are looking for your new fresh ideas on how to make our website communicate what our company does and make us stand out from the rest but is inviting.    We are looking for our new website to be Wordpress.  Our current website is at https://www.lv-meridian.com/ which we are only providing as a reference guide.
LV Meridian Builds and Manages Custom Single-Family Offices please review our website and the New Home Page & Web Designer Instructions for more details. Color scheme -  we would like to follow the same color scheme as our current website.  Provided logo samples as well.

Coding
Coded - Design and coding required
Number of Pages Required
5+ page
Colors
Designer to choose colors to be used in the design.
Requirements
Must have
- 4 P's / Floating Navigation Bar /Stick to the Script

```html
<!DOCTYPE html>
<html lang="en">
<head>
<meta charset="utf-8">
<title>LV Meridian — Family Offices</title>
<link href="https://fonts.googleapis.com/css2?family=Encode+Sans+Condensed:wght@300;400&display=swap" rel="stylesheet">
<style>
:root{
  --navy:#213a6a;
  --navy-deep:#1c3565;
  --sky:#8fd3fb;
  --gold:#f7b52b;
  --yellow:#f5f50a;
  --mint:#3fe3c6;
  --lime:#f2e31a;
  --coral:#f0593a;
  --ink:#222;
  --text:#4a4f5c;
  --white:#fff;
}
*{box-sizing:border-box;margin:0;padding:0}
html,body{width:1200px;height:3018px;overflow:hidden}
body{position:relative;font-family:"Encode Sans Condensed",sans-serif;font-weight:300;color:var(--ink);background:var(--white)}
.abs{position:absolute}
a{color:inherit;text-decoration:none}

/* hero */
.hero{left:0;top:0;width:1200px;height:574px;background:linear-gradient(180deg,#5d7fb5 0%,#9cb3cc 25%,#e8b98f 48%,#c98a5a 60%,#5a6a3a 78%,#2b2f22 100%)}
.brand{left:98px;top:23px;display:flex;align-items:center;gap:14px}
.brand-dot{width:84px;height:84px;border-radius:50%;background:var(--navy)}
.brand-name{font-size:30px;color:var(--navy);font-weight:400}
.nav{right:99px;top:54px;display:flex;gap:30px;font-size:21px;color:var(--navy);font-weight:400}
.hero-title{left:98px;top:220px;font-size:26px;line-height:34px;color:var(--navy);font-weight:400}
.hero-title span{color:#111}
.hero-copy{left:98px;top:304px;width:640px;font-size:19px;line-height:31px;color:#fff}
.btn-service{left:98px;top:387px;width:146px;height:39px;background:var(--gold);color:#fff;font-size:19px;display:flex;align-items:center;justify-content:center}

/* pillars */
.pillar{top:641px;width:317px;height:191px;background:var(--sky);box-shadow:0 12px 10px -6px rgba(0,0,0,.25)}
.pillar-icon{position:absolute;left:17px;top:35px;width:73px;height:120px;background:#fff}
.pillar-title{position:absolute;left:104px;top:33px;font-size:21px;color:#111;font-weight:400}
.pillar-text{position:absolute;left:104px;top:70px;width:196px;font-size:13px;line-height:20.5px;color:#222}
.pillar-text a{color:var(--coral)}

/* philosophy */
.photo-team{left:98px;top:889px;width:404px;height:402px;background:linear-gradient(135deg,#dfe6e8,#c9b6a0 45%,#2a3550 80%);z-index:2}
.office-card{left:184px;top:1028px;width:403px;height:606px;background:var(--navy)}
.counter{position:absolute;left:36px;top:282px;display:flex;align-items:center;gap:8px;color:var(--lime);font-size:54px}
.counter small{font-size:32px}
.office-title{position:absolute;left:36px;top:350px;font-size:24px;color:var(--lime)}
.office-text{position:absolute;left:36px;top:410px;width:340px;font-size:15px;line-height:31px;color:#fff}
.phil-title{left:611px;top:1018px;font-size:42px;color:var(--navy)}
.phil-rule{left:611px;top:1088px;width:490px;height:1px;background:var(--navy)}
.phil-text{left:611px;top:1115px;width:490px;font-size:15px;line-height:31px;color:var(--text)}
.phil-text a{color:var(--coral)}
.mint-rule{left:612px;top:1225px;width:147px;height:2px;background:var(--mint)}
.p-col{top:1243px;width:150px}
.p-col h3{font-size:40px;font-weight:300;color:var(--navy);margin-bottom:14px}
.p-col p{font-size:15px;line-height:31px;color:var(--text)}

/* testimonial */
.testimonial{left:0;top:1698px;width:1200px;height:513px;background:linear-gradient(90deg,#3c3a3c 0%,#6a5d5b 30%,#5c5855 60%,#3b3836 100%)}
.t-title{left:0;width:1200px;top:1756px;text-align:center;font-size:42px;color:#fff}
.play{left:533px;top:1846px}
.quote{left:170px;top:2031px;width:860px;text-align:center;font-size:20px;line-height:31px;color:#fff}

/* process */
.month{left:97px;width:173px;height:45px;border-radius:23px;display:flex;align-items:center;justify-content:center;font-size:19px;color:var(--yellow);background:var(--navy)}
.month.active{background:var(--yellow);color:var(--navy)}
.process-ring{left:328px;top:2287px;width:272px;height:272px;border-radius:50%;background:var(--navy)}
.process-ring::after{content:"";position:absolute;left:38px;top:38px;width:196px;height:196px;border-radius:50%;border:2px dotted #9fd04a}
.process-label{position:absolute;inset:0;display:flex;align-items:center;justify-content:center;text-align:center;font-size:52px;line-height:52px;color:#fff;z-index:1}
.meeting{left:784px;width:316px;height:46px;border-radius:23px;background:var(--yellow);border:1px solid #444;font-size:20px;color:var(--navy);display:flex;align-items:center;padding-left:24px}

/* connect */
.connect{left:0;top:2634px;width:1200px;height:327px;background:var(--navy-deep)}
.c-title{left:0;width:1200px;top:2687px;text-align:center;font-size:42px;color:#fff}
.query{left:357px;top:2783px;width:487px;height:50px;border-radius:25px;background:#fff;border:1px solid #ccc;display:flex;align-items:center;padding-left:25px;font-size:24px;color:#444}
.submit{left:686px;top:2783px;width:158px;height:50px;border-radius:25px;background:var(--yellow);display:flex;align-items:center;justify-content:center;font-size:26px;color:var(--navy)}
.footer{left:0;top:2961px;width:1200px;height:57px;background:#0a0a0a;color:#fff;font-size:14px;display:flex;align-items:center;justify-content:center}
</style>
</head>
<body>

<section class="abs hero" role="img" aria-label="Sunrise over misty mountain ridges with two hot air balloons"></section>
<div class="abs brand"><div class="brand-dot"></div><span class="brand-name">LV Meridian</span></div>
<nav class="abs nav"><a href="#">Home</a><a href="#">About</a><a href="#">Services</a><a href="#">Contact</a></nav>
<h1 class="abs hero-title" style="font-weight:400;font-size:26px">Lorem Ipsum is simply dummy<br><span>text of the printing and typesetting industry.</span></h1>
<p class="abs hero-copy">It is a long established fact that a reader will be distracted by the readable content of a page when looking at its layout. The point of using Lorem Ipsum.</p>
<a class="abs btn-service" href="#">Get Service</a>

<div class="abs pillar" style="left:98px">
  <div class="pillar-icon" role="img" aria-label="Figures celebrating together"></div>
  <div class="pillar-title">Our Mission</div>
  <p class="pillar-text">Lorem ipsum dolor sit amet, consectetur adipiscing elit, sed do eiusmod tempor incididunt ut labore et dolore magna aliqua. <a href="#">Read more...</a></p>
</div>
<div class="abs pillar" style="left:442px">
  <div class="pillar-icon" role="img" aria-label="Two figures embracing"></div>
  <div class="pillar-title">Our Vission</div>
  <p class="pillar-text">Lorem ipsum dolor sit amet, consectetur adipiscing elit, sed do eiusmod tempor incididunt ut labore et dolore magna aliqua. <a href="#">Read more...</a></p>
</div>
<div class="abs pillar" style="left:783px">
  <div class="pillar-icon" role="img" aria-label="Two figures standing side by side"></div>
  <div class="pillar-title">Our Value</div>
  <p class="pillar-text">Lorem ipsum dolor sit amet, consectetur adipiscing elit, sed do eiusmod tempor incididunt ut labore et dolore magna aliqua. <a href="#">Read more...</a></p>
</div>

<div class="abs photo-team" role="img" aria-label="Two colleagues working together in an office"></div>
<div class="abs office-card">
  <div class="counter">
    <svg width="50" height="14" viewBox="0 0 50 14"><path d="M48 7H4M10 1 3 7l7 6" stroke="var(--mint)" stroke-width="3" fill="none"/></svg>
    01 / <small>01</small>
    <svg width="50" height="14" viewBox="0 0 50 14"><path d="M2 7h44M40 1l7 6-7 6" stroke="var(--mint)" stroke-width="3" fill="none"/></svg>
  </div>
  <div class="office-title">What Is a Family Office?</div>
  <p class="office-text">Lorem ipsum dolor sit amet, consectetur adipiscing elit, sed do eiusmod tempor incididunt ut labore et dolore magna aliqua. Quis ipsum suspendisse ultrices gravida. Risus commodo viverra maecenas accumsan lacus vel facilisisrandomised words which don't look even.</p>
</div>
<h2 class="abs phil-title" style="font-weight:300">Investment Phillosophy &amp; Approach</h2>
<div class="abs phil-rule"></div>
<p class="abs phil-text">Lorem ipsum dolor sit amet, consectetur adipiscing elit, sed do eiusmod tempor incididunt ut labore et dolore magna aliqua. Quis ipsum suspendisse ultrices gravida. Risus commodo viverra maecenas accumsan lacus vel facilisis. <a href="#">Read More...</a></p>
<div class="abs mint-rule"></div>
<div class="abs p-col" style="left:611px"><h3>Private</h3><p>Lorem ipsum dolor sit amet, consectetur adipiscing elit, sed do eiusmod tempor incididunt ut labore et dolore magna aliqua. Quis ipsum suspendisse ultrices gravida. Risus commodo viverra maecenas accumsan lacus vel facilisis.</p></div>
<div class="abs p-col" style="left:783px"><h3>Powerful</h3><p>Lorem ipsum dolor sit amet, consectetur adipiscing elit, sed do eiusmod tempor incididunt ut labore et dolore magna aliqua. Quis ipsum suspendisse ultrices gravida. Risus commodo viverra maecenas accumsan lacus vel facilisis.</p></div>
<div class="abs p-col" style="left:953px"><h3>Purposeful</h3><p>Lorem ipsum dolor sit amet, consectetur adipiscing elit, sed do eiusmod tempor incididunt ut labore et dolore magna aliqua. Quis ipsum suspendisse ultrices gravida. Risus commodo viverra maecenas accumsan lacus vel facilisis.</p></div>

<section class="abs testimonial" role="img" aria-label="Portrait of a smiling client in a softly lit room, darkened for text"></section>
<h2 class="abs t-title" style="font-weight:300">Testimonial</h2>
<svg class="abs play" width="134" height="134" viewBox="0 0 134 134"><circle cx="67" cy="67" r="64" fill="none" stroke="#4f8cf5" stroke-width="5"/><path d="M50 38v58l46-29z" fill="none" stroke="#4f8cf5" stroke-width="5" stroke-linejoin="round"/></svg>
<p class="abs quote">"I've led and built family offices from New York to Bermuda to Santiago to Hong Kong.  At LV Meridian, we do things differently—combining rigorous risk management with relentless family focus, and the highest access service possible.  Your office, your way, with our expertise as your edge."<br>— Daniel Marsh, CEO</p>

<div class="abs month active" style="top:2327px">Month 1</div>
<div class="abs month" style="top:2400px">Month 2</div>
<div class="abs month" style="top:2474px">Month 3</div>
<div class="abs process-ring"><div class="process-label">Our<br>Process</div></div>
<svg class="abs" style="left:620px;top:2340px" width="170" height="150" viewBox="0 0 170 150"><path d="M2 43H111V17H164M8 93H164M2 140H111V166" fill="none" stroke="var(--navy)" stroke-width="2"/><path d="M2 140H111V166H164" fill="none" stroke="var(--navy)" stroke-width="2"/></svg>
<svg class="abs" style="left:620px;top:2460px" width="170" height="50" viewBox="0 0 170 50"><path d="M2 20H111V46H164" fill="none" stroke="var(--navy)" stroke-width="2"/></svg>
<div class="abs meeting" style="top:2334px">1. Jacksonville Meting</div>
<div class="abs meeting" style="top:2411px">2. Jacksonville Meting</div>
<div class="abs meeting" style="top:2482px">3. Jacksonville Meting</div>

<section class="abs connect"></section>
<h2 class="abs c-title" style="font-weight:300">Connect With Us</h2>
<div class="abs query">Your Query</div>
<div class="abs submit">Submit</div>
<footer class="abs footer">Copyright 2025@lvmeridianoffices.com. All Rights Are Reserved.</footer>

</body>
</html>
```